K7 Dynamics Stationery Design Project

We are looking to have stationary designs created for our company branding materials. We are looking for the following to be created.
1. Business Cards (front & back)
2. Letterhead
3. Envelopes #10
We are a new web design, development and marketing firm. Primary color scheme is desired to be blue/grey/white. This web start-up is owned and operated by individuals with 15+ years experience each in the industry so should not look as though it is a start-up by young/inexperienced individuals.
We build website & custom applications/software. In addition we provide the full spectrum of web marketing solutions including SEO, PPC, Social Media, Branding, Content Marketing and PR.
Please let us know if you have any questions. Looking forward to seeing all the amazing design ideas.
Attached is our logo.
Thanks!
Target Market(s)
Company will be nearly 100% business to business sales. Looking to work with companies that are already established, with a website, who want to take their website and/or online marketing efforts to the next level.
Industry/Entity Type
Marketing
Look and feel

```html
<!DOCTYPE html>
<html lang="en">
<head>
<meta charset="utf-8">
<title>K7 Dynamics Stationery</title>
<link href="https://fonts.googleapis.com/css2?family=Jost:wght@400;500;600&display=swap" rel="stylesheet">
<style>
  :root {
    --backdrop: #bcbdbf;
    --paper: #e6e7e8;
    --ink: #1f1f1f;
    --panel: #252525;
    --brand-grey: #5d636b;
    --brand-blue: #2f7fd0;
    --card-center: #1ba0dc;
    --card-edge: #2e4987;
    --strip: #334f8c;
    --band: #12a9e8;
    --fold: #1c1c1c;
    --card-text: #3a6aa6;
    --dark-text: #16263c;
    --white: #ffffff;
  }
  * { box-sizing: border-box; margin: 0; padding: 0; }
  html, body { width: 1200px; height: 823px; overflow: hidden; }
  body {
    position: relative;
    background: var(--backdrop);
    font-family: "Jost", "Century Gothic", sans-serif;
  }

  /* Envelope #10 */
  .envelope {
    position: absolute; left: 15px; top: 15px;
    width: 1170px; height: 508px;
    background: var(--paper);
  }
  .envelope__contact {
    position: absolute; left: 29px; top: 455px;
    font-size: 20.5px; color: var(--ink); white-space: nowrap;
  }
  .envelope__brand-panel {
    position: absolute; right: 0; bottom: 0;
    width: 272px; height: 187px;
    background: var(--panel);
    border-top-left-radius: 46px;
  }
  .brand {
    position: absolute; left: 0; right: 0;
    text-align: center; white-space: nowrap;
  }
  .brand__dot {
    display: block; margin: 0 auto 14px;
    width: 22px; height: 22px; border-radius: 50%;
    background: var(--brand-blue);
  }
  .brand__name {
    font-weight: 600; font-size: 21px; color: var(--brand-grey);
    letter-spacing: 0.5px; line-height: 1;
  }
  .brand__tagline {
    font-size: 8px; color: var(--brand-grey); margin-top: 2px;
  }
  .envelope__brand-panel .brand { top: 26px; }
  .envelope__brand-panel .brand__dot { margin-bottom: 58px; }

  /* Business cards */
  .card {
    position: absolute; top: 560px;
    width: 431px; height: 247px; overflow: hidden;
  }
  .card--front {
    left: 156px;
    background: radial-gradient(ellipse 60% 75% at 50% 20%, var(--card-center) 0%, var(--card-edge) 100%);
  }
  .card--front .brand { top: 36px; }
  .card--front .brand__dot { margin-bottom: 62px; }
  .card--front .brand__name { color: #4a5160; }
  .card--front .brand__tagline { color: #3b4452; }
  .card__address {
    position: absolute; left: 0; right: 0; top: 176px;
    text-align: center; font-size: 11px; line-height: 15px;
    color: var(--card-text);
  }

  .card--back {
    left: 613px;
    background: linear-gradient(180deg, #2591d0 0%, #1f86c6 100%);
  }
  .card__strip {
    position: absolute; top: 0; bottom: 0; width: 55px;
    background: linear-gradient(90deg, #2e4884, #3a5a96);
  }
  .card__strip--left { left: 0; }
  .card__strip--right { right: 0; background: linear-gradient(270deg, #2e4884, #3a5a96); }
  .social {
    position: absolute; left: 0; right: 0; top: 25px;
    list-style: none; text-align: center;
  }
  .social__item {
    height: 41px; font-size: 11px; color: var(--white); line-height: 13px;
  }
  .social__mark {
    display: block; margin: 0 auto 2px;
    width: 18px; height: 18px; background: #eaf4fb; border-radius: 2px;
  }
  .name-band {
    position: absolute; left: 37px; top: 170px;
    width: 357px; height: 40px;
    background: var(--band);
    color: var(--white); font-size: 19px; line-height: 40px; text-align: center;
  }
  .name-band__fold { position: absolute; }
  .name-band__fold--top { left: 375px; top: 152px; }
  .name-band__fold--bottom { left: 37px; top: 210px; }
  .card__email {
    position: absolute; left: 0; right: 0; top: 216px;
    text-align: center; font-size: 11px; color: var(--dark-text);
  }
</style>
</head>
<body>

  <section class="envelope" aria-label="Envelope">
    <p class="envelope__contact">1580 W. 92nd Court, Lincoln, NE 68521 | info@k7dynamics.com | www.k7dynamics.com</p>
    <div class="envelope__brand-panel">
      <div class="brand">
        <span class="brand__dot"></span>
        <p class="brand__name">K7 DYNAMICS</p>
        <p class="brand__tagline">Web Design, Development and Marketing</p>
      </div>
    </div>
  </section>

  <section class="card card--front" aria-label="Business card front">
    <div class="brand">
      <span class="brand__dot"></span>
      <p class="brand__name">K7 DYNAMICS</p>
      <p class="brand__tagline">Web Design, Development and Marketing</p>
    </div>
    <p class="card__address">1580 W. 92nd Court, Lincoln, NE 68521<br>info@k7dynamics.com | www.k7dynamics.com</p>
  </section>

  <section class="card card--back" aria-label="Business card back">
    <div class="card__strip card__strip--left"></div>
    <div class="card__strip card__strip--right"></div>
    <ul class="social">
      <li class="social__item"><span class="social__mark"></span>dalemarrow</li>
      <li class="social__item"><span class="social__mark"></span>dale.marrow</li>
      <li class="social__item"><span class="social__mark"></span>dalemarrow</li>
    </ul>
    <svg class="name-band__fold name-band__fold--top" width="19" height="18" viewBox="0 0 19 18">
      <polygon points="0,0 19,18 0,18" fill="var(--fold)"/>
    </svg>
    <div class="name-band">Dale Marrow</div>
    <svg class="name-band__fold name-band__fold--bottom" width="19" height="18" viewBox="0 0 19 18">
      <polygon points="0,0 19,0 19,18" fill="var(--fold)"/>
    </svg>
    <p class="card__email">e-mail: dalemarrow@mailbox.com</p>
  </section>

</body>
</html>
```